Business Card For Security Personal

Stonefield Guard Services is a security company that provides guard services all over Alberta and parts of BC."Our trained professionals, are your best defense!" is our motto.Please see our website www.stonefieldguardservices.example for colours, logos, and a better idea of our image.Thanks!

Industry/Entity Type

Security

Contact Information for Business Card

Stonefield Guard ServicesMartin OkaforPatrol Units Supervisor / SalesPh: 555-418-7362Email: MartinOkafor@stonefieldguardservices.example

```html
<!DOCTYPE html>
<html lang="en">
<head>
<meta charset="utf-8">
<title>Stonefield Guard Services – Business Card</title>
<link rel="stylesheet" href="https://fonts.googleapis.com/css2?family=Arimo:ital,wght@0,400;0,700;1,400&display=swap">
<style>
  :root {
    --stage: #2a2a2a;
    --card-white: #ffffff;
    --card-grey: #c6c6c6;
    --card-black: #232323;
    --accent-blue: #12aee8;
    --accent-yellow: #f4ea1c;
    --ink: #222222;
    --ink-soft: #555555;
    --text-light: #ffffff;
    --mark-grey: #bdbdbd;
  }
  * { box-sizing: border-box; margin: 0; padding: 0; }
  html, body { width: 1200px; height: 750px; overflow: hidden; }
  body {
    background: var(--stage);
    font-family: "Arimo", Arial, sans-serif;
    position: relative;
  }
  .card {
    position: absolute;
    width: 560px;
    height: 320px;
    top: 215px;
    overflow: hidden;
    box-shadow: 0 8px 24px rgba(0,0,0,.45);
  }
  .card--front { left: 30px; background: var(--card-white); }
  .card--back { left: 610px; background: var(--card-grey); }

  .brand {
    position: absolute;
    display: flex;
    align-items: center;
    gap: 12px;
  }
  .brand__square { background: var(--mark-grey); flex: none; }
  .brand__name {
    font-weight: 700;
    color: var(--ink);
    text-transform: uppercase;
    line-height: 1.02;
    letter-spacing: .5px;
  }
  .card--front .brand { left: 150px; top: 100px; }
  .card--front .brand__square { width: 62px; height: 62px; }
  .card--front .brand__name { font-size: 22px; }
  .front__tagline {
    position: absolute;
    left: 0; right: 0; top: 212px;
    text-align: center;
    font-size: 14px;
    color: var(--ink-soft);
  }

  .back__swoosh { position: absolute; inset: 0; }
  .card--back .brand { left: 30px; top: 86px; }
  .card--back .brand__square { width: 50px; height: 50px; }
  .card--back .brand__name { font-size: 18px; }
  .back__tagline {
    position: absolute;
    left: 30px; top: 148px;
    width: 220px;
    font-size: 8.5px;
    font-style: italic;
    color: var(--ink-soft);
    white-space: nowrap;
  }

  .contact {
    position: absolute;
    right: 22px;
    top: 96px;
    text-align: right;
    color: var(--text-light);
  }
  .contact__name { font-size: 18px; font-weight: 700; color: var(--accent-blue); }
  .contact__title { font-size: 12px; margin-top: 3px; }
  .contact__list { list-style: none; margin-top: 16px; }
  .contact__item {
    display: flex;
    justify-content: flex-end;
    align-items: center;
    gap: 6px;
    font-size: 9.5px;
    line-height: 19px;
  }
  .contact__item--phone { font-size: 11px; }
  .contact__icon { width: 11px; height: 11px; fill: var(--accent-blue); flex: none; }
</style>
</head>
<body>

  <section class="card card--front" aria-label="Business card front">
    <div class="brand">
      <span class="brand__square"></span>
      <span class="brand__name">Stonefield<br>Guard<br>Services</span>
    </div>
    <p class="front__tagline">Our trained professionals, are your best defense!</p>
  </section>

  <section class="card card--back" aria-label="Business card back">
    <svg class="back__swoosh" viewBox="0 0 560 320" width="560" height="320" aria-hidden="true">
      <path d="M362,0 C312,40 292,130 257,200 C227,262 152,278 0,290 L0,320 L560,320 L560,0 Z" fill="var(--card-black)"/>
      <path d="M352,0 C302,40 282,130 247,200 C217,262 142,278 0,285" fill="none" stroke="var(--accent-blue)" stroke-width="7"/>
      <path d="M377,0 C327,42 308,132 273,202 C243,266 168,282 0,295" fill="none" stroke="var(--accent-yellow)" stroke-width="3"/>
    </svg>

    <div class="brand">
      <span class="brand__square"></span>
      <span class="brand__name">Stonefield<br>Guard<br>Services</span>
    </div>
    <p class="back__tagline">Our trained professionals, are your best defense!</p>

    <div class="contact">
      <p class="contact__name">Martin Okafor</p>
      <p class="contact__title">Patrol Units Supervisor / Sales</p>
      <ul class="contact__list">
        <li class="contact__item contact__item--phone">555-418-7362
          <svg class="contact__icon" viewBox="0 0 24 24" aria-hidden="true"><path d="M6.6 10.8a15 15 0 0 0 6.6 6.6l2.2-2.2a1 1 0 0 1 1-.25 11.4 11.4 0 0 0 3.6.57 1 1 0 0 1 1 1V20a1 1 0 0 1-1 1A17 17 0 0 1 3 4a1 1 0 0 1 1-1h3.5a1 1 0 0 1 1 1c0 1.250.2 2.450.57 3.57a1 1 0 0 1-.25 1z"/></svg>
        </li>
        <li class="contact__item">MartinOkafor@stonefieldguardservices.example
          <svg class="contact__icon" viewBox="0 0 24 24" aria-hidden="true"><path d="M2 5h20v14H2z M2 5l10 8 10-8" fill="var(--accent-blue)" stroke="var(--card-black)" stroke-width="1.5"/></svg>
        </li>
        <li class="contact__item">www.stonefieldguardservices.example
          <svg class="contact__icon" viewBox="0 0 24 24" aria-hidden="true"><circle cx="12" cy="12" r="11"/><path d="M1 12h22M12 1c4 4 4 18 0 22M12 1c-4 4-4 18 0 22" fill="none" stroke="var(--card-black)" stroke-width="1.5"/></svg>
        </li>
      </ul>
    </div>
  </section>

</body>
</html>
```